Web Design Project for Lark Meadow

We are a Honey Packing Company called Lark Meadow.
We need a new website.
We are open to many ideas.
We want to have headings like: Home/Products/About Us/Contact Us
We want an easy and uncomplicated website.
We need our logo attached to the center top or left top of the webpage.
We want to have a number of our products on the first page that increase in size once the cursor is placed on them.
We want to be able to add photos and products in the future as we expand.
Target Market(s)
Public
Food Distributors
Importers/Exporters
Industry/Entity Type
It Company
Look and feel
Each slider illustrates characteristics of the customer's brand and the style your logo design should communicate.

```html
<!DOCTYPE html>
<html lang="en">
<head>
<meta charset="utf-8">
<title>Lark Meadow – Contact Us</title>
<link rel="stylesheet" href="https://fonts.googleapis.com/css2?family=Rationale&family=Open+Sans:wght@400&display=swap">
<style>
  :root {
    --gold: #f5b800;
    --ink: #111111;
    --field: #000000;
    --rule-grey: #c8c8c8;
    --page: #ffffff;
    --hint: #9a9a9a;
    --alert: #b00000;
    --illustration: #d9d9d9;
    --map-base: #e8e4d8;
    --map-green: #cfe0b0;
  }
  * { box-sizing: border-box; margin: 0; padding: 0; }
  html, body { width: 1200px; height: 595px; overflow: hidden; background: var(--page); }
  body { position: relative; font-family: "Open Sans", sans-serif; color: var(--ink); }

  .rule { position: absolute; height: 1px; }
  .rule--top { top: 7px; left: 0; width: 1200px; background: var(--gold); }
  .rule--gold-left { top: 103px; left: 0; width: 254px; background: var(--gold); }
  .rule--grey { top: 103px; left: 254px; width: 694px; background: var(--rule-grey); }
  .rule--gold-right { top: 103px; left: 948px; width: 252px; background: var(--gold); }

  .brand { position: absolute; top: 14px; left: 393px; width: 400px; text-align: center; font-family: "Rationale", sans-serif; color: var(--ink); }
  .brand__name { font-size: 46px; line-height: 48px; letter-spacing: 2px; text-transform: uppercase; font-weight: 400; }
  .brand__tagline { font-size: 27px; line-height: 30px; }

  .mascot { position: absolute; left: 736px; top: 23px; width: 148px; height: 151px; background: linear-gradient(160deg, var(--illustration), #8a8a8a); border-radius: 40% 40% 20% 20%; }

  .nav { position: absolute; top: 108px; left: 439px; display: flex; gap: 6px; list-style: none; }
  .nav__item { height: 28px; background: var(--gold); font-family: "Rationale", sans-serif; font-size: 13px; line-height: 28px; text-align: center; letter-spacing: 0.5px; color: var(--ink); }
  .nav__item--home { width: 74px; }
  .nav__item--about { width: 74px; }
  .nav__item--products { width: 75px; }
  .nav__item--contact { width: 76px; color: var(--page); }

  .contact-heading { position: absolute; left: 281px; top: 161px; font-size: 22px; font-weight: 400; letter-spacing: 0.3px; }
  .contact-company { position: absolute; left: 281px; top: 193px; font-family: "Rationale", sans-serif; font-size: 15px; text-transform: uppercase; letter-spacing: 0.5px; }
  .contact-address { position: absolute; left: 281px; top: 236px; font-size: 9.5px; line-height: 12px; font-style: normal; }

  .form { position: absolute; left: 516px; top: 186px; width: 404px; }
  .form__field { height: 23px; background: var(--field); color: var(--hint); font-size: 13px; line-height: 23px; padding-left: 5px; margin-bottom: 4px; }
  .form__message { height: 91px; background: var(--field); }
  .form__alert { position: absolute; left: 4px; top: 182px; font-size: 7.5px; color: var(--alert); }
  .form__send { position: absolute; left: 368px; top: 179px; width: 36px; height: 23px; background: var(--field); color: var(--gold); font-size: 12px; line-height: 23px; text-align: center; }

  .map { position: absolute; left: 275px; top: 399px; width: 652px; height: 196px; background: linear-gradient(135deg, var(--map-base) 0%, var(--map-green) 45%, var(--map-base) 100%); }
</style>
</head>
<body>
  <div class="rule rule--top"></div>
  <div class="rule rule--gold-left"></div>
  <div class="rule rule--grey"></div>
  <div class="rule rule--gold-right"></div>

  <header class="brand">
    <h1 class="brand__name">Lark Meadow</h1>
    <p class="brand__tagline">100% Australian Honey</p>
  </header>

  <div class="mascot" role="img" aria-label="Illustration of a seated mascot animal beside the navigation"></div>

  <ul class="nav">
    <li class="nav__item nav__item--home">HOME</li>
    <li class="nav__item nav__item--about">ABOUT US</li>
    <li class="nav__item nav__item--products">PRODUCTS</li>
    <li class="nav__item nav__item--contact">CONTACT US</li>
  </ul>

  <h2 class="contact-heading">CONTACT US</h2>
  <p class="contact-company">Lark Meadow</p>
  <address class="contact-address">
    24 Clover Lane Brookfield<br>
    Hillcrest, SA, Australia 5090<br>
    Tel +61-08-80001234<br>
    Fax +61-08-80001234
  </address>

  <div class="form">
    <div class="form__field">Name</div>
    <div class="form__field">Email</div>
    <div class="form__field">Subject</div>
    <div class="form__message"></div>
    <p class="form__alert">Please add your name</p>
    <div class="form__send">Send</div>
  </div>

  <div class="map" role="img" aria-label="Street map showing the company location"></div>
</body>
</html>
```